Brookvale Systems Yellow rose letterhead

I have a new logo for my company but in its current form it is too large to be used on letterhead or as a email signature. I need to have the designer use elements from the current logo and create something close to the original but more suited for smaller items.
Updates

I just uploaded a copy of our logo that does not have the weathered affect. Thanks

Industry/Entity Type

It Company

Requirements
Must have
• The design must maintain the visual effect of the current logo. It needs to include the yellow rose and the name of the company.
Nice to have
• It would be nice to maintain the stamp theme and incorporate my name, address, phone, email. etc.

```html
<!DOCTYPE html>
<html lang="en">
<head>
<meta charset="utf-8">
<title>Brookvale Systems Letterhead</title>
<link href="https://fonts.googleapis.com/css2?family=Questrial&display=swap" rel="stylesheet">
<style>
  :root {
    --teal: #3cb9bd;
    --paper: #ffffff;
    --ink-light: #ffffff;
  }
  * { margin: 0; padding: 0; box-sizing: border-box; }
  html, body {
    width: 848px;
    height: 1200px;
    overflow: hidden;
    background: var(--paper);
  }
  .letterhead {
    position: relative;
    width: 848px;
    height: 1200px;
    background: var(--paper);
    font-family: "Questrial", sans-serif;
  }
  .header-band {
    position: absolute;
    top: 0;
    left: 0;
    width: 848px;
    height: 220px;
  }
  .header-band path { fill: var(--teal); }
  .sender {
    position: absolute;
    top: 40px;
    left: 45px;
    color: var(--ink-light);
    font-size: 19.5px;
    line-height: 25.5px;
    letter-spacing: 0.4px;
    font-style: normal;
  }
  .company-name {
    position: absolute;
    top: 62px;
    right: 38px;
    display: flex;
    align-items: center;
    gap: 12px;
    color: var(--ink-light);
    font-size: 30px;
    line-height: 34px;
    letter-spacing: 0.5px;
  }
  .company-mark {
    width: 16px;
    height: 16px;
    background: var(--ink-light);
  }
</style>
</head>
<body>
  <main class="letterhead">
    <svg class="header-band" viewBox="0 0 848 220" aria-hidden="true">
      <path d="M0,0 H848 V178 C620,150 260,160 0,214 Z"/>
    </svg>

    <address class="sender">
      Nora Hallett, PhD<br>
      210 W Cedar Ridge Road, Ste 1420<br>
      Millbrook, TX 75900<br>
      1-800-555-0147<br>
      nora@brookvale-systems.com
    </address>

    <div class="company-name">
      <span class="company-mark"></span>
      <span>Brookvale Systems</span>
    </div>
  </main>
</body>
</html>
```